Elegantes und hochwertiges Etiketten-Design für Weinflasche
tulpenwerk hat unsere Anforderungen super umgesetzt und durch eine unkomplizierte und einfache Kommunikation konnten die Feinarbeiten schnell durchgeführt werden. Klasse Arbeit! Gerne wieder :)
Zielgruppe
Wir sind ein liebevoll geführter Familienwinzerbetrieb im schönen Franken, ohne lange Tradition, dafür jung, dynamisch, modern und voller Ideen. Von den eigenen Rebflächen produzieren wir unsere eigenen Weine.
Verantwortlich für den Weinan- und ausbau ist Matthias, stolzer Familienvater und leidenschaftlicher Hobbywinzer. Unterstützt wird er von seiner Familie, von der Verwandtschaft und von seinen Freunden.
Matthias ist hauptberuflich Elektroingenieur, Jongleur von Bits und Bytes. Der Ausgleich zum Beruf ist die Arbeit und Ruhe im Weinberg, immer mit dem Drang, etwas Handwerkliches mit den eigenen Händen umzusetzen.
Was hinter dem Weinausbau steckt ist pure Leidenschaft, Passion zur Perfektion, die Liebe zum Wein und das viele Probieren und Tüfteln im Weinberg und im Weinkeller. Und es ist diese Leidenschaft, die uns immer wieder neu motiviert. Dabei haben wir unser Ziel immer fest im Blick, individuelle Weine, Weine die unsere Handschrift tragen und sehr viel Fruchtpotential und Wiedererkennungswert aufweisen, zu erzeugen.
Zielgruppe:
Genussmenschen, die gerne fruchtige, unkomplizierte und mit unserer Handschrift geprägte Weine genießen wollen.
Aufgabenstellung
- Die Weinflasche (vor allem das Etikett) soll im Weinregal positiv ins Auge stechen und die Aufmerksamkeit des Weingenießer auf die Flasche lenken, aber gleichzeitig elegant und hochwertig wirken. Das Etikett soll beim Weingenießer Emotionen wecken und im Gedächtnis bleiben.
- Als Schlagwort soll „Herzgewitter“ und die Rebsorte „Bacchus“ auf die Vorderseite des Etiketts gedruckt werden. Das Schlagwort soll dabei im Fokus stehen. „Herzgewitter“ steht für die Liebe zwischen mir und meiner Frau, verkörpert in diesem frischen, fruchtigen und lebendigen Bacchus. Da wir dieses Jahr heiraten werden, möchten wir gerne anderen Menschen durch diesen besonderen Wein an unseren „Herzgewitter“ teilhaben lassen
- Im Hintergrund des Etiketts soll ein Bild von mir und meiner Frau als schwarz/weiß Kontur abgebildet sein.
- Das Etikett soll später eventuell mit einer Heißfolienprägung veredelt werden (z.B. Folienprägung von Schlagwort „Herzgewitter“).
- Das Etikett wird in Digitaldruck auf Selbstklebeetiketten gedruckt.
- Flaschenform: Schlegelflasche antikgrün
- Kapsel: schwarzer BVS-Verschluss

```html
<!DOCTYPE html>
<html lang="de">
<head>
<meta charset="utf-8">
<title>Herzgewitter – Etikettenentwurf</title>
<link rel="stylesheet" href="https://fonts.googleapis.com/css2?family=Kaushan+Script&family=Josefin+Sans:wght@400&display=swap">
<style>
  :root {
    --page: #ffffff;
    --paper: #f7f7f7;
    --paper-edge: #e6e6e6;
    --frame: #555555;
    --ink: #2a2a2a;
    --gold-dark: #8a6414;
    --gold: #c9971f;
    --gold-light: #f3d35a;
    --sketch: #d9d9d9;
  }
  * { margin: 0; padding: 0; box-sizing: border-box; }
  html, body {
    width: 1200px; height: 849px; overflow: hidden;
    background: var(--page);
  }
  .sheet { position: relative; width: 1200px; height: 849px; }
  .label {
    position: absolute; top: 113px;
    width: 476px; height: 553px;
    border: 1px solid var(--frame);
    background:
      linear-gradient(90deg, var(--paper-edge) 0%, var(--paper) 8%, #ffffff 40%, #ffffff 70%, var(--paper) 90%, var(--paper-edge) 100%);
    overflow: hidden;
  }
  .label--a { left: 89px; }
  .label--b { left: 605px; }
  .brand {
    position: absolute; top: 34px; left: 0; right: 0;
    text-align: center;
    font-family: "Josefin Sans", sans-serif;
    color: var(--ink);
  }
  .brand__name { font-size: 40px; line-height: 1; letter-spacing: 1px; }
  .brand__sub {
    display: inline-flex; align-items: center; gap: 6px;
    margin-top: 10px;
    font-size: 12px; letter-spacing: 4px;
  }
  .brand__dot {
    width: 14px; height: 14px; border-radius: 50%;
    background: var(--gold);
  }
  .title {
    position: absolute; top: 128px; left: 0; right: 0;
    text-align: center;
    font-family: "Kaushan Script", cursive;
    font-size: 64px; line-height: 1.2;
    background: linear-gradient(100deg, var(--gold-dark) 0%, var(--gold) 25%, var(--gold-light) 45%, var(--gold) 62%, var(--gold-dark) 85%, var(--gold) 100%);
    -webkit-background-clip: text; background-clip: text;
    color: transparent;
  }
  .label--b .title {
    background: linear-gradient(80deg, var(--gold) 0%, var(--gold-dark) 20%, var(--gold-light) 48%, var(--gold-dark) 70%, var(--gold) 100%);
    -webkit-background-clip: text; background-clip: text;
  }
  .portrait {
    position: absolute; left: 84px; top: 247px;
    width: 324px; height: 253px;
    background: radial-gradient(ellipse at center, var(--sketch) 0%, #eeeeee 55%, rgba(255,255,255,0) 80%);
  }
  .foil-band {
    position: absolute; left: 0; right: 0; bottom: 0; height: 20px;
    background: linear-gradient(90deg, var(--gold-dark) 0%, var(--gold) 20%, var(--gold-light) 40%, var(--gold) 55%, var(--gold-light) 70%, var(--gold-dark) 100%);
    border-top: 1px solid var(--frame);
  }
</style>
</head>
<body>
<div class="sheet">
  <section class="label label--a">
    <div class="brand">
      <div class="brand__name">Felsbach</div>
      <div class="brand__sub">WEINBAU <span class="brand__dot"></span></div>
    </div>
    <h1 class="title">Herzgewitter</h1>
    <div class="portrait" role="img" aria-label="Konturzeichnung eines lachenden Paares in Schwarz-Weiß"></div>
    <div class="foil-band"></div>
  </section>

  <section class="label label--b">
    <div class="brand">
      <div class="brand__name">Felsbach</div>
      <div class="brand__sub">WEINBAU <span class="brand__dot"></span></div>
    </div>
    <h1 class="title">Herzgewitter</h1>
    <div class="portrait" role="img" aria-label="Konturzeichnung eines lachenden Paares in Schwarz-Weiß"></div>
    <div class="foil-band"></div>
  </section>
</div>
</body>
</html>
```